Corporate Design für Immobilienverwaltung & -vermittlung
Zielgruppe
Immobilienverwaltung & Vermittlung
Aufgabenstellung
Unser Logo repräsentiert bereits hervorragend unser Markenimage, und ich möchte sicherstellen, dass dies auch in allen anderen Aspekten unserer Kommunikation zum Ausdruck kommt. Daher suche ich nach einem durchgängigen CI Design, das auf dem vorhandenen Logo aufbaut, jedoch ohne Änderungen am Logo selbst.
Konkret benötige ich Unterstützung bei der Gestaltung von:
Visitenkarten
Briefpapier
Briefumschlägen
Stempeln
Flyern
Bannern
und anderen Materialien, die wir in unserer Geschäftskommunikation verwenden.
Das Ziel ist, dass unsere Kunden und Geschäftspartner uns bereits anhand des CI Designs erkennen können, selbst wenn das Logo nicht sofort sichtbar ist. Die Einheitlichkeit von Farben, Schriftarten und Designelementen ist für uns von großer Bedeutung.

```html
<!DOCTYPE html>
<html lang="de">
<head>
<meta charset="utf-8">
<title>Briefumschlag – Brunnfeld Immobilien</title>
<link rel="stylesheet" href="https://fonts.googleapis.com/css2?family=Cormorant+Garamond:wght@500&display=swap">
<style>
  :root {
    --backdrop: #d9d9da;
    --paper: #f4f4f4;
    --paper-edge: #e4e4e4;
    --navy: #1f2a55;
    --navy-deep: #18214a;
  }
  html, body {
    margin: 0;
    padding: 0;
    width: 1200px;
    height: 817px;
    overflow: hidden;
    background: var(--backdrop);
  }
  .canvas {
    position: relative;
    width: 1200px;
    height: 817px;
  }
  .envelope {
    position: absolute;
    left: 110px;
    top: 200px;
    width: 980px;
    height: 490px;
  }
  .envelope-flap {
    position: absolute;
    left: 0;
    top: -96px;
    width: 980px;
    height: 96px;
    border-radius: 26px 26px 0 0;
    background: linear-gradient(180deg, var(--navy) 0%, var(--navy-deep) 100%);
  }
  .envelope-body {
    position: absolute;
    inset: 0;
    background: var(--paper);
    border-bottom: 1px solid var(--paper-edge);
    box-shadow: 0 10px 24px rgba(0, 0, 0, 0.08);
  }
  .brand-name {
    position: absolute;
    left: 0;
    right: 0;
    top: 250px;
    margin: 0;
    text-align: center;
    font-family: "Cormorant Garamond", Georgia, serif;
    font-weight: 500;
    font-size: 34px;
    letter-spacing: 0.06em;
    color: var(--navy);
    font-variant: small-caps;
  }
</style>
</head>
<body>
  <main class="canvas">
    <section class="envelope">
      <div class="envelope-flap" role="img" aria-label="Umschlagklappe mit dunkelblauem Flächenmuster aus hellen Linien"></div>
      <div class="envelope-body">
        <p class="brand-name">Brunnfeld Immobilien</p>
      </div>
    </section>
  </main>
</body>
</html>
```